Nera Bloom Fitness Coaching Project

I am a personal trainer based in London. My services include one-on-one PT sessions, bootcamps.
I would like the design to be minimalistic. With light colours: white, pink, purple.
I specialise in weight loss, flexibility, mobility.

Orla Pemvick
Personal Trainer
Email: orla.pemvick@tovamail.com
tel: 07400918243
Instagram: Nera Bloom

Target Market(s)

adults, mostly females (age 18-50).

Industry/Entity Type

Fitness

Contact Information for Business Card

Orla Pemvick
Personal Trainer
tel: 07400918243
Instagram: Nera Bloom

Font styles to use
Serif

Colors
eea4c8
fbd4d5
fdf9cf
cfeae6
cee9f5

Requirements
Nice to have
• minimalistic style
• easy to read and remember

```html
<!DOCTYPE html>
<html lang="en">
<head>
<meta charset="utf-8">
<title>Nera Bloom Fitness Coaching – Business Card</title>
<link href="https://fonts.googleapis.com/css2?family=Playfair+Display:wght@400;700&family=Noto+Sans:wght@400&display=swap" rel="stylesheet">
<style>
  :root {
    --stage: #0a0a0a;
    --paper: #fcf8f4;
    --ink: #4a4a4a;
    --ink-soft: #666666;
    --ring-blue: #cfe6f1;
    --ring-pink: #f8d0d1;
    --photo-warm: #9a6a45;
    --photo-dark: #4a2c1c;
    --photo-light: #d9b48a;
  }
  * { margin: 0; padding: 0; box-sizing: border-box; }
  html, body {
    width: 1200px; height: 1000px; overflow: hidden;
    background: var(--stage);
  }
  .stage {
    position: relative; width: 1200px; height: 1000px;
    display: flex; align-items: center; justify-content: center; gap: 40px;
  }
  .card {
    position: relative; width: 520px; height: 300px;
    background: var(--paper); border-radius: 20px; overflow: hidden;
  }
  .card-back .rings { position: absolute; inset: 0; }
  .focus-label {
    position: absolute; font-family: "Playfair Display", Georgia, serif;
    font-size: 15px; color: var(--ink-soft);
  }
  .focus-flexibility { left: 178px; top: 38px; }
  .focus-weight-loss { left: 214px; top: 138px; }
  .focus-mobility { left: 262px; top: 232px; }

  .portrait {
    position: absolute; left: 150px; top: 30px; width: 140px; height: 140px;
    border-radius: 50%;
    background: radial-gradient(circle at 50% 45%, var(--photo-light) 0%, var(--photo-warm) 45%, var(--photo-dark) 100%);
  }
  .identity { position: absolute; left: 60px; top: 190px; }
  .identity-name {
    font-family: "Playfair Display", Georgia, serif; font-weight: 700;
    font-size: 24px; color: var(--ink); line-height: 1.1;
  }
  .identity-role {
    font-family: "Noto Sans", Arial, sans-serif; font-size: 13px; color: var(--ink-soft);
  }
  .divider {
    position: absolute; left: 240px; top: 195px; width: 2px; height: 82px;
    background: var(--ink-soft);
  }
  .contacts {
    position: absolute; left: 262px; top: 208px; list-style: none;
    font-family: "Noto Sans", Arial, sans-serif; font-size: 14px; color: var(--ink);
  }
  .contacts li { display: flex; align-items: center; gap: 8px; height: 22px; }
  .contact-icon { width: 16px; height: 16px; flex: none; }
</style>
</head>
<body>
<main class="stage">
  <section class="card card-back" aria-label="Card back: areas of focus">
    <svg class="rings" viewBox="0 0 520 300" aria-hidden="true">
      <circle cx="250" cy="140" r="170" fill="none" stroke="var(--ring-blue)" stroke-width="5"/>
      <circle cx="250" cy="146" r="78" fill="none" stroke="var(--ring-pink)" stroke-width="5"/>
    </svg>
    <span class="focus-label focus-flexibility">Flexibility</span>
    <span class="focus-label focus-weight-loss">Weight Loss</span>
    <span class="focus-label focus-mobility">Mobility</span>
  </section>

  <section class="card card-front" aria-label="Card front: contact details">
    <div class="portrait" role="img" aria-label="Portrait photo of the trainer with long curly hair"></div>
    <div class="identity">
      <h1 class="identity-name">Orla Pemvick</h1>
      <p class="identity-role">Personal Trainer</p>
    </div>
    <div class="divider"></div>
    <ul class="contacts">
      <li>
        <svg class="contact-icon" viewBox="0 0 16 16" aria-hidden="true">
          <circle cx="8" cy="8" r="8" fill="var(--ink)"/>
          <path d="M5.5 4.5l1.3 0 .6 1.8-.9.7a5 5 0 0 0 2.5 2.5l.7-.9 1.8.6 0 1.3c-3.5.3-6.3-2.5-6-6z" fill="var(--paper)"/>
        </svg>
        07 40 09 18 243
      </li>
      <li>
        <svg class="contact-icon" viewBox="0 0 16 16" aria-hidden="true">
          <circle cx="8" cy="8" r="8" fill="var(--ink)"/>
          <rect x="4.2" y="5.2" width="7.6" height="5.6" fill="none" stroke="var(--paper)" stroke-width="1.1"/>
          <path d="M4.4 5.4L8 8.2l3.6-2.8" fill="none" stroke="var(--paper)" stroke-width="1.1"/>
        </svg>
        orla.pemvick@tovamail.com
      </li>
      <li>
        <svg class="contact-icon" viewBox="0 0 16 16" aria-hidden="true">
          <circle cx="8" cy="8" r="8" fill="var(--ink)"/>
        </svg>
        Nera Bloom
      </li>
    </ul>
  </section>
</main>
</body>
</html>
```